Neues Etikett für Wasch- und Reinigungspaste
Es hat uns gefreut! Eine tolle Zusammenarbeit und ein wunderbares Ergebnis!
Zielgruppe
KANDOMIR, das sind wir, Spezialisten in Hygiene und Gastronomiebedarf. Wir stellen Reinigungsmittel im oberösterreichischen Mühlviertel (Aigen-Schlägl) her und wir beraten, planen und bieten die komplette Einrichtung von Gastronomieküchen an.
Unsere Hygieneprodukte tragen dazu bei, dass sich Menschen in einem Gebäude wohl fühlen. Denn Sauberkeit und Hygiene sind Faktoren, die für unsere Gesundheit wichtig sind. Die Zielgruppen im Bereich Reinigungsmittel sind Eigenheimbesitzer, Wohnraum-Mieter und in Betrieben das Reinigungspersonal bzw. die verantworlichen Mitarbeiter für die Objekthygiene.
Aufgabenstellung
Kurz: Wir suchen für ein altes Produkt ein neues Etikett. Das Produkt heißt „Tovira“ und ist eine Wasch- und Reinigungspaste / Schmierseife, also ein altbewährtes Hausmittel, dass auch heute noch wunderbar vielseitig einsetzbar ist. Wir möchten ihr Image gerne etwas aufpeppen, da es unserer Meinung nach im Allgemeinen und auch bei uns zu stiefmütterlich auftritt. Wir denken, dass sie mehr in den Mittelpunkt rücken sollte, gerade da sie in vielen Fällen andere Reinigungsmittel ersetzen kann und auch durch ihre Ergiebigkeit die Umwelt entlastet.
Wir haben uns bewusst dazu entschieden, das alte Etikett hier nicht mit hochzuladen, daß heißt hier soll es keinen Wiedererkennungswert zu anderen Kandomir-Produkten geben. Bitte orientieren Sie sich allein an diesem Briefing.
Das Produkt ist sehr nachhaltig, ergiebig und damit sparsam. Erhältlich ist es in einem weißen, runden 5 kg Eimer (siehe Upload). Das Endformat des Etiketts auf dem weissen Eimer beträgt maximal 150 mm (H) x 170 mm (B). Es ist auch in kleineren und größeren Einheiten erhältlich, jedoch wird das Etikett dann durch uns angepasst.
Es ist wichtig, dass auf den ersten Blick sichtbar ist, dass es sich um eine Wasch- und Reinigungspaste handelt. Sie reinigt zum Beispiel Geschirr, Besteck, Aluminium, Glas, lackierte Möbel, Kunststoffmöbel, Fliesen, Waschbecken, Badewannen, Fahrzeuge, Maschinen, schmierige Hände, Holz- und Kunststoffböden, Feinwäsche, Wolle, Seide, Vorhänge, zum Einweichen und Vorwaschen von Arbeits- und Buntwäsche. Anwendung: 1 Esslöffel auf 10 Liter Wasser oder auch pur anwendbar je nach Einsatzbereich. Enthält keine Phosphate und ist biologisch abbaubar. Inhalt: 5 kg

```html
<!DOCTYPE html>
<html lang="de">
<head>
<meta charset="utf-8">
<title>TOVIRA – Etikett Wasch-/Reinigungspaste</title>
<link href="https://fonts.googleapis.com/css2?family=Josefin+Sans:wght@300;400;600&family=Mrs+Saint+Delafield&display=swap" rel="stylesheet">
<style>
  :root {
    --navy: #042e40;
    --red: #d8141c;
    --green: #66b345;
    --ink: #2b2b2b;
    --icon: #8d9296;
    --paper: #ffffff;
  }
  html, body {
    margin: 0;
    padding: 0;
    width: 848px;
    height: 1200px;
    overflow: hidden;
    background: var(--paper);
  }
  .canvas {
    position: relative;
    width: 848px;
    height: 1200px;
    font-family: "Josefin Sans", sans-serif;
  }
  .label {
    position: absolute;
    left: 124px;
    top: 129px;
    width: 585px;
    height: 501px;
    background: var(--paper);
    box-shadow: 0 18px 30px rgba(0, 0, 0, 0.18);
  }
  .usage-text {
    position: absolute;
    left: 9px;
    top: 34px;
    margin: 0;
    font-size: 10.6px;
    line-height: 13.3px;
    font-weight: 300;
    color: var(--ink);
  }
  .feature-panel {
    position: absolute;
    left: 183px;
    top: 0;
    width: 233px;
    height: 210px;
    background: var(--navy);
  }
  .slogan {
    position: absolute;
    left: 0;
    right: 0;
    top: 40px;
    margin: 0;
    text-align: center;
    font-family: "Mrs Saint Delafield", cursive;
    font-weight: 400;
    font-size: 54px;
    color: var(--red);
    transform: rotate(-8deg);
  }
  .usage-icons {
    position: absolute;
    left: 16px;
    top: 149px;
    display: flex;
    gap: 8px;
  }
  .usage-icons svg {
    width: 27px;
    height: 27px;
    display: block;
  }
  .eco-badge {
    position: absolute;
    left: 467px;
    top: 30px;
    width: 70px;
    height: 70px;
    border-radius: 50%;
    background: var(--green);
  }
  .eco-text {
    position: absolute;
    left: 439px;
    top: 106px;
    margin: 0;
    font-size: 10.6px;
    line-height: 13.3px;
    font-weight: 300;
    color: var(--ink);
  }
  .product-name {
    position: absolute;
    left: 0;
    right: 0;
    top: 236px;
    margin: 0;
    text-align: center;
    font-size: 96px;
    font-weight: 600;
    line-height: 1;
    letter-spacing: 1px;
    color: var(--navy);
  }
  .product-type {
    position: absolute;
    left: 0;
    right: 0;
    top: 335px;
    margin: 0;
    text-align: center;
    font-size: 19px;
    font-weight: 300;
    color: var(--red);
  }
  .brand {
    position: absolute;
    left: 0;
    right: 0;
    top: 420px;
    display: flex;
    justify-content: center;
    align-items: center;
    gap: 10px;
  }
  .brand-dot {
    width: 16px;
    height: 16px;
    border-radius: 50%;
    background: var(--red);
  }
  .brand-name {
    font-size: 30px;
    font-weight: 400;
    letter-spacing: 1px;
    color: var(--navy);
  }
  .content {
    position: absolute;
    left: 496px;
    top: 437px;
    margin: 0;
    font-weight: 300;
    color: var(--ink);
    line-height: 1;
  }
  .content-label {
    display: block;
    font-size: 18px;
  }
  .content-value {
    display: block;
    margin-top: 4px;
    font-size: 32px;
  }
</style>
</head>
<body>
<div class="canvas">
  <section class="label">
    <p class="usage-text">
      Lorem ipsum dolor sit amet,<br>
      consectetuer adipiscing elit,<br>
      sed diam nonummy nibh<br>
      euisLorem ipsum dolor sit<br>
      amet, consectetuer<br>
      adipiscing elit, sed diam<br>
      nonummy nibh euismod<br>
      tincidunt ut laoreet dolore<br>
      magna aliquam erat volutpat.<br>
      Ut wisi enim Lorem ipsum<br>
      dolor sit amet, consectetuer<br>
      adipiscing elit, sed diam<br>
      nonummy nibh euismod
    </p>

    <div class="feature-panel">
      <h2 class="slogan">Ihr Slogan</h2>
      <div class="usage-icons">
        <svg viewBox="0 0 27 27" aria-label="Geschirr">
          <rect x="0.6" y="0.6" width="25.8" height="25.8" rx="4" fill="none" stroke="var(--icon)" stroke-width="1"/>
          <path d="M5 14h10l-1.5 8h-7z" fill="none" stroke="var(--icon)" stroke-width="1"/>
          <rect x="14" y="5" width="7" height="8" rx="1" fill="none" stroke="var(--icon)" stroke-width="1"/>
        </svg>
        <svg viewBox="0 0 27 27" aria-label="Fahrzeuge">
          <rect x="0.6" y="0.6" width="25.8" height="25.8" rx="4" fill="none" stroke="var(--icon)" stroke-width="1"/>
          <path d="M5 17v-4l2.5-4h12l2.5 4v4z" fill="var(--icon)"/>
          <circle cx="9" cy="18" r="2" fill="var(--navy)" stroke="var(--icon)"/>
          <circle cx="18" cy="18" r="2" fill="var(--navy)" stroke="var(--icon)"/>
        </svg>
        <svg viewBox="0 0 27 27" aria-label="Haushalt">
          <rect x="0.6" y="0.6" width="25.8" height="25.8" rx="4" fill="none" stroke="var(--icon)" stroke-width="1"/>
          <path d="M4 13l9.5-8 9.5 8" fill="none" stroke="var(--icon)" stroke-width="1.4"/>
          <path d="M7 12v10h13v-10" fill="var(--icon)"/>
          <rect x="11.5" y="16" width="4" height="6" fill="var(--navy)"/>
        </svg>
        <svg viewBox="0 0 27 27" aria-label="pH-Wert">
          <rect x="0.6" y="0.6" width="25.8" height="25.8" rx="4" fill="none" stroke="var(--icon)" stroke-width="1"/>
          <text x="5" y="8" font-size="5" fill="var(--icon)" font-family="Josefin Sans, sans-serif">0</text>
          <text x="5" y="15" font-size="5" fill="var(--icon)" font-family="Josefin Sans, sans-serif">7</text>
          <text x="4" y="22" font-size="5" fill="var(--icon)" font-family="Josefin Sans, sans-serif">14</text>
          <line x1="13" y1="4" x2="13" y2="20" stroke="var(--icon)" stroke-width="1"/>
          <text x="16" y="22" font-size="5.5" fill="var(--icon)" font-family="Josefin Sans, sans-serif">pH</text>
        </svg>
        <svg viewBox="0 0 27 27" aria-label="Dosierung 10 Liter">
          <rect x="0.6" y="0.6" width="25.8" height="25.8" rx="4" fill="none" stroke="var(--icon)" stroke-width="1"/>
          <path d="M10 5l3 4" stroke="var(--icon)" stroke-width="1"/>
          <path d="M5 12h17l-2 10h-13z" fill="var(--icon)"/>
          <text x="8.5" y="19" font-size="5" font-weight="600" fill="var(--paper)" font-family="Josefin Sans, sans-serif">10 l</text>
        </svg>
        <svg viewBox="0 0 27 27" aria-label="Böden">
          <rect x="0.6" y="0.6" width="25.8" height="25.8" rx="4" fill="none" stroke="var(--icon)" stroke-width="1"/>
          <path d="M4 14h10l-1.5 8h-7z" fill="none" stroke="var(--icon)" stroke-width="1"/>
          <path d="M21 4l-4 16" stroke="var(--icon)" stroke-width="1.2"/>
          <path d="M14 22l3-3 4 3z" fill="var(--icon)"/>
        </svg>
      </div>
    </div>

    <div class="eco-badge" role="img" aria-label="Umweltsiegel: biologisch abbaubar"></div>
    <p class="eco-text">
      Lorem ipsum dolor sit amet,<br>
      consectetuer adipiscing elit,<br>
      sed diam nonummy nibh
    </p>

    <h1 class="product-name">TOVIRA</h1>
    <p class="product-type">Wasch-/Reinigungspaste . Schmierseife</p>

    <div class="brand">
      <span class="brand-dot"></span>
      <span class="brand-name">KANDOMIR</span>
    </div>

    <p class="content">
      <span class="content-label">Inhalt</span>
      <span class="content-value">5 L</span>
    </p>
  </section>
</div>
</body>
</html>
```